Website Re-design

Hi, I'm looking for help in redesigning my web site. I currently have a site www.brightnookwares.example where I sell lamps, and while I like some aspects of the design, you can tell that I have done the graphics myself and am not a pro at it. I'd like help in redesigning it, and am open to completely new design graphics. I have made the 3 slider images myself, and I feel they could be a bit better, but I am not sure how to do it. For example, on the homepage, the 'About Us', 'Secured Shopping', and '$10 Off' graphics don't go well with the rest of the page. I would like more cohesion in the design and more visual interest in the header, which is pretty basic right now. Also, that the bottom footer is black, I would like instead something else. I am looking for just the layout of the homepage, and possibly once that is done to work on more visual interest in some of the informational pages and product pages. I am looking for just the design in the form of a photoshop file or files that I can incorporate into my site. Thank you!

Reason: I just made this project payment committed, so I'd like a chance for designers who only choose payment committed projects to submit artwork. Thank you.

This project is now payment guaranteed/ committed.  Thanks.

```html
<!DOCTYPE html>
<html lang="en">
<head>
<meta charset="utf-8">
<title>Brightnook Lighting – Home</title>
<link href="https://fonts.googleapis.com/css2?family=Lobster&family=Open+Sans:wght@400;600;700&family=Libre+Baskerville&display=swap" rel="stylesheet">
<style>
:root{
  --ink:#3a3a3a;
  --muted:#8a8a8a;
  --line:#dcdcdc;
  --topbar:#f1f1f1;
  --nav-active:#4a4a4a;
  --orange:#e2531f;
  --teal:#3aa7c9;
  --red:#d9262c;
  --green:#7cc24a;
  --footer:#ececec;
  --photo:#eeeeee;
  --white:#ffffff;
}
*{box-sizing:border-box;margin:0;padding:0}
html,body{width:784px;height:1200px;overflow:hidden;background:var(--white)}
body{font-family:"Open Sans",sans-serif;color:var(--ink);font-size:10px;position:relative}
.wrap{width:640px;margin:0 auto;position:relative}

.topbar{height:30px;background:var(--topbar);border-bottom:1px solid var(--line)}
.topbar .wrap{display:flex;justify-content:flex-end;align-items:center;height:30px;gap:14px;font-size:8px;color:var(--muted)}
.topbar .signin{font-weight:700;color:var(--ink)}
.search{width:96px;height:16px;border:1px solid var(--line);background:var(--white);font-size:7px;color:var(--muted);padding:2px 5px;display:flex;justify-content:space-between;align-items:center}

.header{height:80px}
.header .wrap{height:80px}
.brand{position:absolute;left:0;top:14px;display:flex;align-items:center;gap:8px}
.brand-mark{width:22px;height:22px;border-radius:50%;background:var(--nav-active)}
.brand-name{font-size:18px;font-weight:600;color:var(--nav-active);line-height:1}
.utility{position:absolute;right:0;top:10px;display:flex;align-items:center;gap:8px;font-size:8px}
.cart{background:var(--white);border:1px solid var(--line);padding:3px 8px;display:flex;gap:5px;align-items:center}
.cart b{color:var(--red)}
.checkout{border:1px solid var(--ink);padding:3px 8px;font-weight:600}
.nav{position:absolute;right:0;bottom:0;display:flex;font-size:9px;font-weight:600;letter-spacing:.5px}
.nav a{display:block;padding:10px 14px;color:var(--ink);text-decoration:none;border-left:1px solid var(--line)}
.nav a.active{background:var(--nav-active);color:var(--white)}

.hero{height:425px;position:relative;overflow:hidden}
.hero-photo{position:absolute;inset:0;background:linear-gradient(180deg,#4a1a3e 0%,#6e2859 45%,#8a6a80 75%,#c9c1ba 100%)}
.hero-copy{position:absolute;left:150px;top:50px;color:var(--white);text-align:center;width:230px}
.hero-title{font-family:"Lobster",cursive;font-size:64px;line-height:1;text-shadow:0 2px 4px rgba(0,0,0,.3)}
.hero-title span{display:block}
.hero-sub{font-family:"Libre Baskerville",serif;font-size:14px;margin-top:40px;white-space:nowrap;margin-left:-40px;margin-right:-40px}
.hero-btn{display:inline-block;margin-top:16px;background:var(--orange);color:var(--white);font-family:"Libre Baskerville",serif;font-size:13px;padding:8px 14px;box-shadow:0 2px 4px rgba(0,0,0,.3)}
.dots{position:absolute;bottom:12px;left:50%;transform:translateX(-50%);display:flex;gap:6px}
.dots i{width:6px;height:6px;border-radius:50%;background:#9d9690}
.dots i.on{background:var(--white)}

.features{display:flex;justify-content:space-between;margin-top:14px}
.feature{width:190px;text-align:center}
.feature-tab{height:58px;position:relative;display:flex;align-items:flex-end;justify-content:center;padding-bottom:8px;color:var(--white);font-family:"Lobster",cursive;font-size:21px}
.feature-tab svg{position:absolute;top:-22px;left:50%;margin-left:-20px}
.feature.about .feature-tab{background:var(--teal)}
.feature.secure .feature-tab{background:var(--red)}
.feature.offer .feature-tab{background:var(--green)}
.feature p{font-size:8px;line-height:1.5;color:var(--muted);padding:10px 10px 6px}
.feature .more{display:inline-block;font-size:6px;color:var(--white);padding:3px 7px;font-weight:700}
.feature.about .more{background:var(--teal)}
.feature.secure .more{background:var(--red)}
.feature.offer .more{background:var(--green)}

.products-title{margin-top:30px;display:flex;align-items:center;gap:14px;font-family:"Lobster",cursive;font-size:22px;color:var(--ink)}
.products-title::before,.products-title::after{content:"";flex:1;height:1px;background:var(--line)}
.products{display:flex;justify-content:space-between;margin-top:10px}
.product{width:150px}
.product-photo{height:170px;background:var(--photo)}
.product h3{font-size:8px;font-weight:600;margin-top:8px}
.product .price{font-size:8px;color:var(--red);margin-top:2px}
.view-more{margin-top:14px;display:flex;align-items:center;gap:10px;font-size:7px;color:var(--muted)}
.view-more::before,.view-more::after{content:"";flex:1;height:1px;background:var(--line)}

.footer{position:absolute;left:0;right:0;bottom:0;height:172px;background:var(--footer)}
.footer .wrap{display:flex;gap:34px;padding-top:18px}
.footer h4{font-size:7px;font-weight:700;margin-bottom:6px;letter-spacing:.3px}
.footer li{list-style:none;font-size:7px;color:var(--muted);line-height:1.7}
.signup{margin-left:auto;width:190px}
.signup-row{display:flex}
.signup-row span{flex:1;height:16px;border:1px solid var(--line);background:var(--white);font-size:6px;color:var(--muted);padding:3px 5px}
.signup-row b{background:#222;color:var(--white);font-size:6px;padding:4px 8px}
.signup p{font-size:6px;color:var(--muted);margin-top:4px}
.social{display:flex;gap:6px;margin-top:8px}
.social i{width:18px;height:18px;border-radius:50%;display:block}
.copyright{position:absolute;bottom:8px;left:0;right:0;text-align:center;font-size:6px;color:var(--muted);border-top:1px solid var(--line);padding-top:8px;width:640px;margin:0 auto}
</style>
</head>
<body>
<header>
  <div class="topbar"><div class="wrap">
    <span class="signin">Sign in</span><span>Create an account</span><span>My account</span>
    <span class="search">Search <span>&#9906;</span></span>
  </div></div>
  <div class="header"><div class="wrap">
    <div class="brand"><span class="brand-mark"></span><span class="brand-name">Brightnook Lighting</span></div>
    <div class="utility">
      <span class="cart">Shopping Cart <b>0</b></span>
      <span>&#9825; Wishlist</span>
      <span class="checkout">Checkout</span>
    </div>
    <nav class="nav"><a href="#">HOME</a><a href="#" class="active">SHOP</a><a href="#">ABOUT US</a><a href="#">CONTACT US</a></nav>
  </div></div>
</header>

<section class="hero">
  <div class="hero-photo" role="img" aria-label="Photo of a purple crystal table lamp with a white shade on a wooden floor against a purple wall"></div>
  <div class="hero-copy">
    <div class="hero-title"><span>A Touch</span><span style="font-size:50px">of</span><span>Class</span></div>
    <div class="hero-sub">"The Violet Facet" Table Lamp</div>
    <span class="hero-btn">SHOP ALL LAMPS</span>
  </div>
  <div class="dots"><i></i><i class="on"></i><i></i></div>
</section>

<main class="wrap">
  <section class="features">
    <div class="feature about">
      <div class="feature-tab">
        <svg width="40" height="40" viewBox="0 0 40 40"><circle cx="20" cy="20" r="19" fill="var(--teal)" stroke="#fff" stroke-width="2"/><circle cx="20" cy="15" r="5" fill="#fff"/><path d="M11 29c1-6 5-8 9-8s8 2 9 8z" fill="#fff"/></svg>
        About Us
      </div>
      <p>Brightnook Lighting provides beautiful and artistic home and hospitality lighting.</p>
      <span class="more">READ MORE</span>
    </div>
    <div class="feature secure">
      <div class="feature-tab">
        <svg width="40" height="40" viewBox="0 0 40 40"><circle cx="20" cy="20" r="19" fill="var(--red)" stroke="#fff" stroke-width="2"/><rect x="11" y="13" width="18" height="13" rx="1" fill="none" stroke="#fff" stroke-width="2"/><path d="M11 17h18" stroke="#fff" stroke-width="2"/></svg>
        Secured Shopping
      </div>
      <p>Shopping at Brightnook Lighting is secured and protected by industry standard best practices.</p>
      <span class="more">READ MORE</span>
    </div>
    <div class="feature offer">
      <div class="feature-tab">
        <svg width="40" height="40" viewBox="0 0 40 40"><circle cx="20" cy="20" r="19" fill="var(--green)" stroke="#fff" stroke-width="2"/><path d="M12 13h9l8 8-8 8-9-9z" fill="none" stroke="#fff" stroke-width="2"/><circle cx="16" cy="17" r="1.6" fill="#fff"/></svg>
        $10 Off
      </div>
      <p>$10 off any purchase when you sign up for our newsletter.</p>
      <span class="more">SIGN UP</span>
    </div>
  </section>

  <h2 class="products-title">Our Products</h2>
  <section class="products">
    <article class="product">
      <div class="product-photo" role="img" aria-label="Product photo: turquoise glass table lamp"></div>
      <h3>Lagoon Medium Table Lamp</h3><div class="price">$199.00</div>
    </article>
    <article class="product">
      <div class="product-photo" role="img" aria-label="Product photo: faceted purple crystal table lamp"></div>
      <h3>Violet Facet Table Lamp</h3><div class="price">$219.00</div>
    </article>
    <article class="product">
      <div class="product-photo" role="img" aria-label="Product photo: patterned porcelain table lamp"></div>
      <h3>Meadow Porcelain Table Lamp</h3><div class="price">$209.00</div>
    </article>
    <article class="product">
      <div class="product-photo" role="img" aria-label="Product photo: dark teal glass table lamp"></div>
      <h3>Harbor Table Lamp</h3><div class="price">$189.00</div>
    </article>
  </section>
  <div class="view-more">View More</div>
</main>

<footer class="footer">
  <div class="wrap">
    <div><h4>HELP + INFO</h4><ul><li>Contact Us</li><li>Shipping Info</li><li>Returns</li><li>To The Trade</li><li>Privacy Policy</li><li>Terms of Use</li></ul></div>
    <div><h4>MY ACCOUNT</h4><ul><li>Sign In</li><li>Order Status</li><li>Order History</li><li>Wish List</li><li>Checkout</li></ul></div>
    <div><h4>ABOUT</h4><ul><li>Who We Are</li><li>Testimonials</li></ul></div>
    <div><h4>CONTACT</h4><ul><li>Contact Us</li><li>hello@brightnookwares.example</li></ul></div>
    <div class="signup">
      <h4>SIGN UP FOR BRIGHTNOOK LIGHTING EMAILS</h4>
      <div class="signup-row"><span>Enter email address</span><b>SIGN UP</b></div>
      <p>Be the first to hear about new lamps and offers.</p>
      <div class="social"><i style="background:#3b5998"></i><i style="background:#35a9de"></i><i style="background:#cb2027"></i></div>
    </div>
  </div>
  <div class="copyright">© 2013 Brightnook Lighting · www.brightnookwares.example · All Rights Reserved.</div>
</footer>
</body>
</html>
```